Outdoor Company Business Card design

We are an outdoor adventure company needing a business card. We sell outdoor adventures and clothing. Please use our logo in the business card. We are looking for something unique but delivers a clear message as to who we are. Please be creative

Target Market(s)

Outdoor adventures

Industry/Entity Type

Business

Contact Information for Business Card

Business name: TrailBirch If using the logo, no need to have a spot for the name
Owner / CEO: Ross Dalby
Website: TrailBirch.example
Facebook: Facebook.com/TrailBirch
Instagram: @dalby_ross
phone number: 555-304-7192
Email: Dalbycrew@TrailBirch.example

Colors

Designer to choose colors to be used in the design.

Requirements
Must have
• The business card must include the details mentioned above. ie logo, my name, email, facebook, instagram, website, and phone number.
Should not have
• should not be cluttered or look messy

```html
<!DOCTYPE html>
<html lang="en">
<head>
<meta charset="utf-8">
<title>TrailBirch Business Card</title>
<link rel="stylesheet" href="https://fonts.googleapis.com/css2?family=Montserrat:wght@600;700&family=Roboto:wght@400&display=swap">
<style>
  :root {
    --backdrop: #c4c4c4;
    --front-dark: #141414;
    --front-mid: #2a2a2a;
    --brand-blue: #2d5fa3;
    --brand-blue-light: #3f86d6;
    --brand-orange: #d0541c;
    --card-light: #ededed;
    --ink: #2b2b2b;
    --white: #ffffff;
  }
  * { box-sizing: border-box; margin: 0; padding: 0; }
  html, body {
    width: 1200px; height: 1138px; overflow: hidden;
    background: var(--backdrop);
  }
  .card {
    position: absolute;
    width: 620px; height: 374px;
    border-radius: 14px;
    overflow: hidden;
    box-shadow: 0 3px 8px rgba(0,0,0,.3);
  }
  /* Front */
  .card-front {
    left: 274px; top: 186px;
    background: radial-gradient(ellipse at 40% 30%, var(--front-mid) 0%, var(--front-dark) 70%);
  }
  .brand-name {
    font-family: "Montserrat", sans-serif;
    font-weight: 700;
    letter-spacing: 1px;
    line-height: 1;
  }
  .card-front .brand-name {
    position: absolute; left: 0; right: 0; top: 150px;
    text-align: center;
    font-size: 66px;
    color: var(--brand-blue-light);
  }
  .front-base-band {
    position: absolute; left: 0; bottom: 0;
    width: 100%; height: 8px;
    background: var(--brand-blue);
  }
  .front-web-tab {
    position: absolute; right: 0; bottom: 0;
    width: 296px; height: 33px;
    background: var(--brand-orange);
    clip-path: polygon(16px 0, 100% 0, 100% 100%, 0 100%);
    display: flex; align-items: center; justify-content: center;
    padding-left: 12px;
    font-family: "Roboto", sans-serif; font-size: 16px;
    color: var(--white);
  }
  .social-row {
    position: absolute;
    display: flex; align-items: center; gap: 8px;
    font-family: "Roboto", sans-serif; font-size: 16px;
  }
  .card-front .social-row { left: 33px; top: 336px; color: #e6e6e6; }
  .social-dot {
    width: 15px; height: 15px; border-radius: 50%; flex: none;
  }
  .dot-blue { background: var(--brand-blue); }
  .dot-orange { background: var(--brand-orange); }
  .social-row .gap { width: 6px; }

  /* Back */
  .card-back {
    left: 276px; top: 608px;
    background: linear-gradient(135deg, #f3f3f3, #e3e3e3);
  }
  .back-side-band {
    position: absolute; left: 0; top: 0; bottom: 0;
    width: 61px; background: var(--brand-blue);
  }
  .back-side-rule {
    position: absolute; left: 65px; top: 0; bottom: 0;
    width: 5px; background: var(--brand-orange);
  }
  .card-back .brand-name {
    position: absolute; left: 90px; top: 118px;
    font-size: 50px;
    color: var(--brand-blue);
  }
  .person {
    position: absolute; left: 92px; top: 210px;
    display: flex; align-items: baseline; gap: 22px;
  }
  .person-name {
    font-family: "Montserrat", sans-serif; font-weight: 700;
    font-size: 30px; letter-spacing: 1px;
    color: var(--brand-blue);
  }
  .person-name .surname { color: var(--brand-orange); }
  .person-role {
    font-family: "Roboto", sans-serif; font-size: 16px; color: var(--ink);
  }
  .contact-list {
    position: absolute; left: 92px; top: 253px;
    list-style: none;
    font-family: "Roboto", sans-serif; font-size: 17px; color: var(--ink);
  }
  .contact-list li {
    display: flex; align-items: center; gap: 11px;
    height: 23.5px;
  }
  .contact-list svg { width: 15px; height: 15px; flex: none; }
  .card-back .social-row { left: 91px; top: 332px; color: var(--ink); font-size: 17px; }
</style>
</head>
<body>

<section class="card card-front" aria-label="Card front">
  <div class="brand-name">TrailBirch</div>
  <div class="social-row">
    <span class="social-dot dot-blue"></span><span>/TrailBirch</span>
    <span class="gap"></span>
    <span class="social-dot dot-orange"></span><span>@dalby_ross</span>
  </div>
  <div class="front-base-band"></div>
  <div class="front-web-tab">www.TrailBirch.example</div>
</section>

<section class="card card-back" aria-label="Card back">
  <div class="back-side-band"></div>
  <div class="back-side-rule"></div>
  <div class="brand-name">TrailBirch</div>
  <div class="person">
    <span class="person-name">ROSS <span class="surname">DALBY</span></span>
    <span class="person-role">Owner / CEO</span>
  </div>
  <ul class="contact-list">
    <li>
      <svg viewBox="0 0 16 16" aria-hidden="true"><path fill="#d0541c" d="M2 6c0-2 3-3 6-3s6 1 6 3v1h-3V5.5H5V7H2z M4 8h8l1 5H3z"/></svg>
      <span>555-304-7192</span>
    </li>
    <li>
      <svg viewBox="0 0 16 16" aria-hidden="true"><rect x="1" y="3" width="14" height="10" fill="#d0541c"/><path d="M1.5 3.5 8 9l6.5-5.5" fill="none" stroke="#fff" stroke-width="1.3"/></svg>
      <span>www.TrailBirch.example</span>
    </li>
    <li>
      <svg viewBox="0 0 16 16" aria-hidden="true"><g fill="none" stroke="#d0541c" stroke-width="1.4"><circle cx="8" cy="8" r="6.3"/><ellipse cx="8" cy="8" rx="2.8" ry="6.3"/><path d="M1.7 8h12.6M2.8 5h10.4M2.8 11h10.4"/></g></svg>
      <span>Dalbycrew@TrailBirch.example</span>
    </li>
  </ul>
  <div class="social-row">
    <span class="social-dot dot-blue"></span><span>/TrailBirch</span>
    <span class="gap"></span>
    <span class="social-dot dot-orange"></span><span>@dalby_ross</span>
  </div>
</section>

</body>
</html>
```